The Warden needs a book cover for his new book, VALTORNESHADE.

A full size picture of his face. A black hood covers everything but his face, a mask which horizontally cuts his face in half below his nose and stretching from ear to ear, with the top half a reproduction of the American flag with the stars around the right eye and the stripes continuing across. Below his nose and ears, extending across the lower half of his face, all in solid black with white highlighted skeleton-looking teeth and facial bones.The mask should be all one piece, as if it was painted on. The eyes are blue holding love and fury in them.Book title VALTORNESHADE below the head, unsure of color, perhaps red, white and blue 0r silver with bold font.

Font styles to use
Sans Serif

Requirements
Must have
• see project description
• Powerful blue eyes
Nice to have
• perhaps a darker gray background so the hood stands out
• some good ideas to make it pop

```html
<!DOCTYPE html>
<html lang="en">
<head>
<meta charset="utf-8">
<title>VALTORNESHADE — Book Cover</title>
<link href="https://fonts.googleapis.com/css2?family=Bebas+Neue&family=Cinzel:wght@400;500&family=EB+Garamond:wght@400&family=Oswald:wght@600&display=swap" rel="stylesheet">
<style>
  :root {
    --navy-deep: #070b1d;
    --navy: #0d1533;
    --navy-mid: #1a2550;
    --flag-red: #b3283a;
    --flag-white: #e8e6ea;
    --title-red: #b0141b;
    --title-red-dark: #5a0508;
    --text-white: #f3f3f5;
    --hood-black: #111215;
    --hood-grey: #2a2c33;
    --face-grey: #6d6f76;
    --glow-red: #ff1a1a;
    --novel-blue: #1c3fd0;
  }
  * { margin: 0; padding: 0; box-sizing: border-box; }
  html, body {
    width: 1200px; height: 864px; overflow: hidden;
    background: var(--navy-deep);
  }
  .cover-wrap {
    position: relative; width: 1200px; height: 864px;
    display: flex;
  }

  /* Back cover */
  .back-cover {
    position: relative; width: 565px; height: 864px;
    background: linear-gradient(180deg, var(--navy-mid) 0%, var(--navy) 35%, var(--navy-deep) 100%);
    overflow: hidden;
  }
  .back-flag-art {
    position: absolute; left: 0; top: 0; width: 565px; height: 170px;
    background: linear-gradient(180deg, rgba(190,70,90,.75) 0%, rgba(120,60,100,.55) 45%, rgba(13,21,51,0) 100%),
                linear-gradient(90deg, #27356e 0%, #27356e 42%, rgba(200,190,200,.6) 60%, rgba(180,60,80,.5) 100%);
  }
  .back-figure-art {
    position: absolute; left: 150px; top: 300px; width: 415px; height: 564px;
    background: radial-gradient(ellipse at 70% 55%, rgba(60,75,120,.35) 0%, rgba(13,21,51,0) 70%);
  }
  .back-title {
    position: absolute; left: 62px; top: 146px; width: 455px;
    font-family: "Bebas Neue", "Oswald", sans-serif;
    font-size: 92px; line-height: 1; letter-spacing: 1px;
    color: var(--title-red);
    text-shadow: 3px 3px 0 var(--title-red-dark), 0 0 8px rgba(0,0,0,.6);
    text-align: center;
  }
  .back-blurb {
    position: absolute; left: 62px; top: 248px; width: 452px;
    font-family: "EB Garamond", Georgia, serif;
    font-size: 14.2px; line-height: 1.47;
    color: var(--text-white); text-align: justify;
  }
  .back-blurb p + p { margin-top: 20px; }
  .back-tagline {
    position: absolute; left: 40px; top: 626px; width: 500px;
    font-family: "Cinzel", "Times New Roman", serif;
    font-size: 29px; line-height: 1.18; letter-spacing: 3px;
    color: var(--text-white); text-align: center;
  }

  /* Spine */
  .spine {
    position: relative; width: 67px; height: 864px;
    background: linear-gradient(90deg, #050814 0%, #0b1230 50%, #050814 100%);
  }
  .spine-text {
    position: absolute; left: 50%; top: 45px;
    transform: translateX(-50%);
    writing-mode: vertical-rl;
    display: flex; align-items: center; gap: 22px;
  }
  .spine-title {
    font-family: "Bebas Neue", "Oswald", sans-serif;
    font-size: 40px; letter-spacing: 1px; color: var(--title-red);
    text-shadow: 2px 2px 0 var(--title-red-dark);
  }
  .spine-author {
    font-family: "Cinzel", "Times New Roman", serif;
    font-size: 34px; letter-spacing: 4px; color: var(--text-white);
  }

  /* Front cover */
  .front-cover {
    position: relative; width: 568px; height: 864px;
    background: linear-gradient(180deg, #0c1533 0%, #0a0f22 60%, #070a17 100%);
    overflow: hidden;
  }
  .front-hooded-figure {
    position: absolute; left: 0; top: 0; width: 568px; height: 864px;
  }
  .front-title {
    position: absolute; left: 0; top: 578px; width: 568px;
    font-family: "Bebas Neue", "Oswald", sans-serif;
    font-size: 100px; line-height: 1; letter-spacing: 1px;
    color: var(--title-red); text-align: center;
    text-shadow: 3px 3px 0 var(--title-red-dark), 0 0 10px rgba(0,0,0,.7);
  }
  .front-glow-line {
    position: absolute; left: 0; top: 690px; width: 568px; height: 24px;
  }
  .front-author {
    position: absolute; left: 0; top: 730px; width: 568px;
    font-family: "Cinzel", "Times New Roman", serif;
    font-size: 37px; letter-spacing: 5px; color: var(--text-white);
    text-align: center;
  }
  .front-novel {
    position: absolute; left: 0; top: 822px; width: 568px;
    font-family: "Oswald", sans-serif; font-weight: 600;
    font-size: 18px; letter-spacing: 1.5px; color: var(--novel-blue);
    text-align: center;
  }
</style>
</head>
<body>
<div class="cover-wrap">

  <section class="back-cover">
    <div class="back-flag-art" role="img" aria-label="Waving American flag fading into dark blue"></div>
    <div class="back-figure-art" role="img" aria-label="Faint shadowed silhouette of the hooded figure"></div>
    <h2 class="back-title">VALTORNESHADE</h2>
    <div class="back-blurb">
      <p>What doesn’t kill you will make you stronger. In my case that is true, but it also created my alter ego. You see, as difficult as it was for me to trust and be able to love, learning to hate was so much easier. I guess that’s just human nature.</p>
      <p>My wife’s senseless death along with the ensuing media circus propelled me down a path that I could never have imagined and one where no one, especially in the media, will ever forget.</p>
      <p>I have learned many things on my journey to find justice for my wife, Sweetness. None more important than the fact that you are either defined by your situation or you define it, creating who I am and, more importantly, who I would become. My love for my wife forged who I was as a man. What happened to her forged what I became as a monster.</p>
      <p>It wouldn’t take long before my vow of justice would morph into a thirst for vengeance. I gave the Justice System a chance and they failed. People’s actions have consequences!</p>
    </div>
    <p class="back-tagline">ONE PERSON CAN<br>CHANGE THE WORLD</p>
  </section>

  <section class="spine">
    <div class="spine-text">
      <span class="spine-title">VALTORNESHADE</span>
      <span class="spine-author">DORIAN HALVORSEN</span>
    </div>
  </section>

  <section class="front-cover">
    <svg class="front-hooded-figure" viewBox="0 0 568 864" role="img" aria-label="Hooded figure in a black hood with an American flag painted over the upper face, blue eyes and a skeletal lower jaw">
      <defs>
        <radialGradient id="hood-fill" cx="50%" cy="35%" r="60%">
          <stop offset="0%" stop-color="#2a2c33"/>
          <stop offset="70%" stop-color="#141519"/>
          <stop offset="100%" stop-color="#0a0b0e"/>
        </radialGradient>
        <radialGradient id="face-fill" cx="50%" cy="45%" r="55%">
          <stop offset="0%" stop-color="#7a6a78"/>
          <stop offset="60%" stop-color="#4a4650"/>
          <stop offset="100%" stop-color="#1a1a1f"/>
        </radialGradient>
      </defs>
      <path d="M60 864 C40 600 90 330 150 190 C200 70 300 40 380 70 C470 110 520 230 540 400 C560 560 555 720 568 864 Z" fill="url(#hood-fill)"/>
      <ellipse cx="300" cy="320" rx="150" ry="200" fill="url(#face-fill)"/>
    </svg>
    <h1 class="front-title">VALTORNESHADE</h1>
    <svg class="front-glow-line" viewBox="0 0 568 24" preserveAspectRatio="none" aria-hidden="true">
      <defs>
        <linearGradient id="line-fade" x1="0" x2="1">
          <stop offset="0" stop-color="#ff1a1a" stop-opacity=".35"/>
          <stop offset=".5" stop-color="#ff2a2a" stop-opacity="1"/>
          <stop offset="1" stop-color="#ff1a1a" stop-opacity=".35"/>
        </linearGradient>
        <radialGradient id="spark" cx="50%" cy="50%" r="50%">
          <stop offset="0" stop-color="#ffffff"/>
          <stop offset=".3" stop-color="#ff4040"/>
          <stop offset="1" stop-color="#ff0000" stop-opacity="0"/>
        </radialGradient>
      </defs>
      <rect x="0" y="6" width="568" height="3" fill="url(#line-fade)"/>
      <rect x="0" y="14" width="568" height="2" fill="url(#line-fade)" opacity=".7"/>
      <ellipse cx="284" cy="11" rx="60" ry="10" fill="url(#spark)"/>
    </svg>
    <p class="front-author">DORIAN HALVORSEN</p>
    <p class="front-novel">A NOVEL?</p>
  </section>

</div>
</body>
</html>
```